I created a company name KORUNO and I sell cell phone cases. I'm interesting for a great package and

I need a packaging design for a new company based in Quebec City called KORUNO. I have a supplier in China and I need a good design for my cell phones cases product. I want a black design with a red. The final design should tell the customer I WANT TO BUY THAT CASE.

Target Market(s)

Everyone who has a cell phone

Industry/Entity Type

Cell Phone

Font styles to use
Sans Serif
Other font styles liked:
• I want script original to stand out from the competition

Colors

Designer to choose colors to be used in the design.

Requirements
Must have
• Black and red. I want have look like the photo I just send. I want it with red. Just look at the photo and try to design similar like this, but not the same.
Nice to have
• My company name in the middle. I want it in white. Design me a packaging cases I feel like I want to buy it.

```html
<!DOCTYPE html>
<html lang="en">
<head>
<meta charset="utf-8">
<title>KORUNO Phone Cover Packaging</title>
<link href="https://fonts.googleapis.com/css2?family=Archivo+Black&family=Archivo:wght@700&display=swap" rel="stylesheet">
<style>
  :root {
    --pack-red: #ec1c24;
    --ink-black: #000000;
    --paper-white: #ffffff;
    --icon-orange: #f7941d;
    --case-slate: #47536f;
    --case-slate-dark: #2f3850;
  }
  html, body {
    margin: 0;
    padding: 0;
    overflow: hidden;
    background: var(--paper-white);
  }
  .canvas {
    position: relative;
    width: 999px;
    height: 1200px;
    overflow: hidden;
    background: var(--paper-white);
  }
  .package-art {
    position: absolute;
    inset: 0;
  }
  .brand-name {
    position: absolute;
    left: 0;
    width: 999px;
    top: 212px;
    text-align: center;
    font-family: "Archivo Black", "Archivo", sans-serif;
    font-size: 92px;
    line-height: 1;
    letter-spacing: 2px;
    color: var(--ink-black);
    margin: 0;
  }
  .product-label {
    position: absolute;
    left: 258px;
    top: 435px;
    width: 74px;
    text-align: center;
    font-family: "Archivo", sans-serif;
    font-weight: 700;
    font-size: 18px;
    line-height: 1;
    color: var(--ink-black);
    margin: 0;
  }
</style>
</head>
<body>
  <div class="canvas">
    <svg class="package-art" width="999" height="1200" viewBox="0 0 999 1200" xmlns="http://www.w3.org/2000/svg">
      <defs>
        <linearGradient id="caseTone" x1="0" y1="0" x2="1" y2="1">
          <stop offset="0" stop-color="var(--case-slate)"/>
          <stop offset="1" stop-color="var(--case-slate-dark)"/>
        </linearGradient>
      </defs>

      <!-- hanger tab -->
      <path class="hanger-tab" d="M215 35 H785 V136 H215 Z" fill="var(--pack-red)"/>
      <rect class="hanger-slot" x="390" y="78" width="204" height="27" rx="13.5" fill="var(--paper-white)"/>

      <!-- box front -->
      <rect class="box-front" x="205" y="135" width="590" height="1033" fill="var(--pack-red)"/>

      <!-- chevron band -->
      <path class="chevron-band" d="M468 323 H535 L795 622 V952 L500 362 L205 955 V622 Z" fill="var(--ink-black)"/>

      <!-- product window -->
      <path class="product-window" role="img" aria-label="Photo of a slate blue rugged phone case with black bumper edges and camera cut-out"
            d="M500 400 L697 800 V1040 Q697 1070 667 1070 H327 Q297 1070 297 1040 V800 Z"
            fill="url(#caseTone)"/>

      <!-- phone icon -->
      <rect class="phone-icon" x="261" y="316" width="68" height="84" rx="6" fill="var(--ink-black)" stroke="var(--icon-orange)" stroke-width="3"/>
      <rect class="phone-icon-screen" x="268" y="324" width="54" height="62" fill="var(--ink-black)" stroke="var(--icon-orange)" stroke-width="1.5"/>
      <circle class="phone-icon-button" cx="295" cy="393" r="3.5" fill="var(--pack-red)"/>
    </svg>

    <h1 class="brand-name">KORUNO</h1>
    <p class="product-label">COVER</p>
  </div>
</body>
</html>
```